Full book cover for suspenseful mystery with a cool private investigator

I need a full cover (front, spine, and back) for a mystery set in the mountains, involving sabotage (explosions) at mining sites. The "hero" is a private investigator from the foothills of Alberta (think ranch country) who travels to the mountains and is embroiled in the investigation. His "sidekick" is his black T340. I'd like a sense of suspense and danger on the cover, perhaps the hero leaning on his truck (?) but no front face view so readers can imagine the hero their own way. Current cover is uploaded below. I think it may not convey "Mystery and Private Investigator" enough. Front Cover should have title: The Quiet Ledger; subtitle: A Vorstane Mystery; and Author name: Henrietta Balcombe. I can supply back cover copy etc later.
Updates

After one designer asked for more detail I realized my brief was probably not that helpful to designers. So I have expanded the brief to give designers more information that might help them come up with ideas. I have added the extra information as a document attached to the brief. Thanks so much to everyone who is submitting - and I apologize for not providing sufficient info at the beginninng.

Target Market(s)

mystery readers who are attracted to suspenseful intriguing mysteries

Industry/Entity Type

Books

Font styles to use
Sans Serif

Colors

Designer to choose colors to be used in the design.

Requirements
Must have
• a hint of mountains; a sense of danger; the colours and fonts typical of mystery covers contrasting colours please; san serif, blocky font. The title should grab the eye.
Nice to have
• detective (he wears a leather bomber jacket, jeans, cowboy boots)
Should not have
• avoid military type action covers

```html
<!DOCTYPE html>
<html lang="en">
<head>
<meta charset="utf-8">
<title>The Quiet Ledger — Full Cover</title>
<link rel="stylesheet" href="https://fonts.googleapis.com/css2?family=Anton&family=Teko:wght@300;500&family=Tinos:ital,wght@0,400;0,700;1,400;1,700&display=swap">
<style>
  :root{
    --title-red:#ea2c26;
    --ink-white:#ffffff;
    --copy-white:#eef3f4;
    --mist:#a9cfd6;
    --sky-top:#7fb0bb;
    --sky-mid:#4d7c88;
    --ridge:#2f545e;
    --forest:#152a31;
    --ground:#081216;
    --fire:#f06a24;
    --ember:#ffb347;
    --fuse:#e4ef6a;
  }
  html,body{margin:0;padding:0;overflow:hidden;background:var(--ground);}
  .cover{
    position:relative;width:1200px;height:857px;overflow:hidden;
    font-family:"Tinos","Times New Roman",serif;color:var(--copy-white);
  }

  /* artwork area: soft tonal gradients only */
  .cover-art{
    position:absolute;inset:0;
    background:
      /* ember glow of the burning cabin and ground fire */
      radial-gradient(ellipse 110px 55px at 690px 625px, rgba(255,140,50,.85), rgba(240,106,36,.35) 55%, transparent 100%),
      radial-gradient(ellipse 130px 22px at 850px 665px, rgba(240,106,36,.75), transparent 100%),
      radial-gradient(ellipse 260px 90px at 760px 650px, rgba(240,106,36,.28), transparent 100%),
      /* headlight haze at the right edge */
      radial-gradient(ellipse 90px 60px at 1150px 600px, rgba(210,230,235,.35), transparent 100%),
      /* lit fuse spark on the back */
      radial-gradient(circle 34px at 175px 655px, rgba(240,250,150,.95), rgba(228,239,106,.45) 45%, transparent 100%),
      /* bright misty sky glow among the peaks */
      radial-gradient(ellipse 520px 260px at 880px 60px, rgba(190,225,232,.75), transparent 75%),
      radial-gradient(ellipse 380px 180px at 420px 30px, rgba(160,205,215,.45), transparent 75%),
      /* valley mist band */
      radial-gradient(ellipse 700px 110px at 800px 470px, rgba(169,207,214,.45), transparent 80%),
      /* dark forest framing on the left and lower edge */
      linear-gradient(90deg, rgba(6,14,18,.92) 0%, rgba(8,18,22,.55) 18%, rgba(8,18,22,.12) 42%, rgba(8,18,22,0) 60%),
      linear-gradient(180deg, transparent 0%, transparent 58%, rgba(6,14,18,.7) 80%, rgba(4,10,12,.95) 100%),
      linear-gradient(180deg, var(--sky-top) 0%, var(--sky-mid) 28%, var(--ridge) 48%, var(--forest) 70%, var(--ground) 100%);
  }

  /* back cover */
  .back{
    position:absolute;left:80px;top:68px;width:386px;
    font-size:14.6px;line-height:20.6px;text-align:justify;
  }
  .back p{margin:0 0 20px;}
  .blurb{margin-top:54px;text-align:left;}
  .blurb p{margin:0 0 20px;}
  .blurb .source{display:block;}
  .blurb .source-name{text-transform:uppercase;}

  .publisher{
    position:absolute;display:flex;flex-direction:column;align-items:center;gap:5px;
    font-family:"Teko",sans-serif;font-weight:500;font-size:14px;line-height:.95;
    color:var(--ink-white);text-transform:uppercase;letter-spacing:.5px;text-align:center;
  }
  .publisher .mark{width:16px;height:16px;border-radius:50%;background:var(--ink-white);}
  .publisher--back{left:40px;top:732px;width:70px;}
  .publisher--spine{left:570px;top:732px;width:70px;}

  /* spine */
  .spine-text{
    position:absolute;writing-mode:vertical-rl;
    text-transform:uppercase;line-height:1;
  }
  .spine-author{
    left:582px;top:32px;font-family:"Teko",sans-serif;font-weight:300;
    font-size:34px;letter-spacing:2px;color:var(--ink-white);
  }
  .spine-title{
    left:583px;top:328px;font-family:"Anton",sans-serif;
    font-size:31px;letter-spacing:2.5px;color:var(--title-red);
  }

  /* front cover */
  .title{
    position:absolute;left:0;top:0;margin:0;
    font-family:"Anton",sans-serif;font-weight:400;color:var(--title-red);
    text-transform:uppercase;
  }
  .title span{
    position:absolute;display:block;width:420px;left:732px;text-align:center;
    line-height:.86;white-space:nowrap;
  }
  .title .t1{top:58px;font-size:86px;}
  .title .t2{top:144px;font-size:128px;}
  .title .t3{top:268px;font-size:128px;}

  .subtitle{
    position:absolute;left:722px;top:412px;width:400px;text-align:center;margin:0;
    font-family:"Teko",sans-serif;font-weight:300;font-size:58px;line-height:1;
    letter-spacing:2px;text-transform:uppercase;color:var(--ink-white);
  }
  .author{
    position:absolute;left:775px;top:704px;width:300px;text-align:center;margin:0;
    font-family:"Anton",sans-serif;font-size:54px;line-height:1.04;
    text-transform:uppercase;color:var(--ink-white);letter-spacing:1px;
  }
</style>
</head>
<body>
<main class="cover">
  <div class="cover-art" role="img" aria-label="Misty teal mountain range above a dark pine forest; on the back a lit fuse sparks in the grass; on the front a cabin burns beside a ground fire while a man in a hat and long coat, seen from behind, stands near a black pickup truck"></div>

  <section class="back">
    <p>Some promises are killers to keep.</p>
    <p>Private investigator Gabe Vorstane can name a hundred places he’d rather visit than Harrowmere, British Columbia. But a promise is a promise. The trip should be a cameo: check in, attend a christening, check out. Two days, max. What can go wrong in two days?</p>
    <p>When a burned body is discovered at a sabotaged mine site near the small town, and police finger his kid brother as their prime suspect, Gabe realizes he’s not getting out of Harrowmere quickly, or easily. His battle to save his recalcitrant brother’s neck pits Gabe against deceptive locals, a mountain’s secrets, and a cunning killer who ultimately threatens to destroy all Gabe cares about and pushes him to his breaking point.</p>
    <p>What can go wrong in two days? Everything.</p>
    <div class="blurb">
      <p>“<b><i>The Quiet Ledger</i></b> is just the beginning to an addictive new series.”
        <span class="source"><span class="source-name">Desmond Tolliver</span>, National Ledger Best Selling Author of</span>
        <i>The Marla Quennell Series</i></p>
      <p><b>“Sharp and pitch perfect”</b>
        <span class="source"><span class="source-name">Wren A. Castellane</span>, award-winning author of <b><i>Afterlight</i></b></span></p>
    </div>
  </section>
  <div class="publisher publisher--back"><span class="mark"></span>Kestrel<br>Press</div>

  <div class="spine-text spine-author">Henrietta Balcombe</div>
  <div class="spine-text spine-title">The Quiet Ledger</div>
  <div class="publisher publisher--spine"><span class="mark"></span>Kestrel<br>Press</div>

  <h1 class="title"><span class="t1">The</span><span class="t2">Quiet</span><span class="t3">Ledger</span></h1>
  <p class="subtitle">A Vorstane Mystery</p>
  <p class="author">Henrietta<br>Balcombe</p>
</main>
</body>
</html>
```